Thank you cards for online orders

We have a logo that is attached and I'd for it to be used to make a thank you card that will give our clients some info on product care as well as refund/exchange policy. so maybe a small package that includes a thank you card, and policy details
Updates

Sick

Target Market(s)

Females for 20-70

```html
<!DOCTYPE html>
<html lang="en">
<head>
<meta charset="utf-8">
<title>Lunavale – Thank You Card</title>
<link rel="stylesheet" href="https://fonts.googleapis.com/css2?family=Jost:wght@400;500;600&family=Libre+Baskerville&family=Kristi&display=swap">
<style>
  :root {
    --page: #ffffff;
    --card: #ffffff;
    --leaf: #a6c43e;
    --leaf-soft: #dfeab8;
    --leaf-wash: #eef4d9;
    --sage: #8e9c8f;
    --text: #8f9a8e;
    --shadow: rgba(60, 70, 50, 0.28);
  }
  * { margin: 0; padding: 0; box-sizing: border-box; }
  html, body { width: 985px; height: 1200px; overflow: hidden; background: var(--page); }
  .canvas { position: relative; width: 985px; height: 1200px; }

  .card {
    position: absolute;
    left: 58px;
    width: 865px;
    height: 496px;
    background: var(--card);
    box-shadow: 4px 6px 12px var(--shadow);
    overflow: hidden;
  }
  .card--front { top: 62px; }
  .card--back { top: 619px; }

  .wash {
    position: absolute; inset: 0;
    background:
      radial-gradient(ellipse 340px 90px at 30% 0%, var(--leaf-soft), transparent 70%),
      radial-gradient(ellipse 300px 80px at 80% 4%, var(--leaf-wash), transparent 70%),
      radial-gradient(ellipse 380px 80px at 25% 100%, var(--leaf-soft), transparent 70%),
      radial-gradient(ellipse 360px 90px at 75% 100%, var(--leaf-wash), transparent 70%);
  }

  .ornament {
    position: absolute;
    top: 30px;
    width: 152px;
    height: 450px;
  }
  .ornament--left {
    left: 0;
    background: radial-gradient(ellipse 150px 225px at 0% 50%, var(--leaf) 0%, var(--leaf-soft) 60%, transparent 100%);
  }
  .ornament--right {
    right: 0;
    background: radial-gradient(ellipse 150px 225px at 100% 50%, var(--leaf) 0%, var(--leaf-soft) 60%, transparent 100%);
  }

  .brand {
    position: absolute;
    left: 0; right: 0;
    text-align: center;
  }
  .brand__name {
    font-family: 'Jost', sans-serif;
    font-weight: 400;
    font-size: 44px;
    letter-spacing: 3px;
    color: var(--leaf);
    line-height: 1;
  }
  .brand__est {
    margin-top: 12px;
    font-family: 'Libre Baskerville', serif;
    font-size: 12px;
    letter-spacing: 2px;
    color: var(--sage);
  }
  .card--front .brand { top: 64px; }
  .card--back .brand { top: 373px; }

  .thanks {
    position: absolute;
    top: 160px; left: 0; right: 0;
    text-align: center;
    font-family: 'Kristi', cursive;
    font-size: 128px;
    line-height: 1;
    color: var(--sage);
    letter-spacing: 4px;
  }

  .site {
    position: absolute;
    top: 408px; left: 0; right: 0;
    text-align: center;
    font-family: 'Jost', sans-serif;
    font-size: 28px;
    letter-spacing: 5px;
    color: var(--leaf);
  }

  .policy {
    position: absolute;
    top: 54px; left: 50px; right: 50px;
    text-align: center;
    font-family: 'Jost', sans-serif;
    color: var(--text);
  }
  .policy__title {
    font-size: 20px;
    font-weight: 600;
    letter-spacing: 0.5px;
    line-height: 28px;
  }
  .policy__body {
    font-size: 20.5px;
    font-weight: 500;
    line-height: 27.5px;
  }
</style>
</head>
<body>
<main class="canvas">
  <section class="card card--front">
    <div class="wash"></div>
    <div class="ornament ornament--left" role="img" aria-label="Green line-art mandala ornament at the left edge"></div>
    <div class="ornament ornament--right" role="img" aria-label="Green line-art mandala ornament at the right edge"></div>
    <div class="brand">
      <div class="brand__name">LUNAVALE</div>
      <div class="brand__est">EST. 2006</div>
    </div>
    <h1 class="thanks">Thank you</h1>
    <div class="site">www.lunavale.com</div>
  </section>

  <section class="card card--back">
    <div class="wash"></div>
    <div class="policy">
      <h2 class="policy__title">REFUNDS</h2>
      <p class="policy__body">
        Once we receive the item(s) they will be inspected, and an email will<br>
        be sent to notify you of the approval or rejection of your refund.<br>
        If you are approved, then your refund will be processed minus a<br>
        re-stocking fee of 10% and a credit will automatically be issued in<br>
        your original method of payment, within 5-10 business days.<br>
        Why a re-stocking fee? Lunavale charges a 10% restocking fee to<br>
        help cover any processing fees, handling, and other costs associa-<br>
        ted with processing returns.
      </p>
    </div>
    <div class="brand">
      <div class="brand__name">LUNAVALE</div>
      <div class="brand__est">EST. 2006</div>
    </div>
  </section>
</main>
</body>
</html>
```